A Pinloop Ad design to promote Laptops / Zentrix

I need a Pinloop ad design (modifications to the attached file) . The laptop image needs to be a vector/illustration.Cannot use Zentrix actual image. Colour theme to remain as White, Black Grey (as per this image). Ad text [1st Line : For SME Business only! 2nd Line : Buy a new laptop with KWD Grant subsidy. 3rd line: Message us to find out more!] The overall feel should be similar to this image attached. As for the color/image in the laptop - pls try to suggest something similar to what Corvel uses for their ad.

Font styles to use
Sans Serif

Requirements
Must have
• The laptop image needs to be a vector/illustration.Cannot use Zentrix actual image. Colour theme to remain as White, Black Grey (as per this image). Ad text [1st Line : For SME Business only! 2nd Line : Buy a new laptop with KWD Grant subsidy. 3rd line: Message us to find out more!] The overall feel should be similar to this image attached.

```html
<!DOCTYPE html>
<html lang="en">
<head>
<meta charset="UTF-8">
<title>Pinloop Ad – KWD Grant Laptop Offer</title>
<link rel="stylesheet" href="https://fonts.googleapis.com/css2?family=Montserrat:wght@300;400;500;900&display=swap">
<style>
  :root {
    --stage: #a7a8ac;
    --banner-wide: #f4f4f5;
    --banner-box: #ffffff;
    --ink: #1c1c1c;
    --muted: #6e6e6e;
    --screen-a: #22b8fd;
    --screen-b: #8ff6fb;
    --body-a: #b3b4b7;
    --body-b: #d6d7da;
  }
  * { margin: 0; padding: 0; box-sizing: border-box; }
  html, body {
    width: 1200px; height: 1200px; overflow: hidden;
    background: var(--stage);
    font-family: "Montserrat", Arial, sans-serif;
  }
  .canvas { position: relative; width: 1200px; height: 1200px; }
  .banner { position: absolute; overflow: hidden; }
  .banner--wide { left: 197px; top: 199px; width: 828px; height: 315px; background: var(--banner-wide); }
  .banner--box { left: 288px; top: 608px; width: 640px; height: 360px; background: var(--banner-box); }

  .headline {
    position: absolute; font-weight: 900; color: var(--ink);
    letter-spacing: 0.2px; white-space: nowrap; line-height: 1;
  }
  .subline {
    position: absolute; font-weight: 300; color: var(--muted);
    letter-spacing: 0.8px; white-space: nowrap; line-height: 1.25;
  }
  .cta {
    position: absolute; display: flex; align-items: center; gap: 9px;
    color: var(--ink); font-weight: 400; letter-spacing: 0.5px; white-space: nowrap;
  }
  .cta__brand { font-weight: 400; }

  .laptop-art {
    position: absolute;
    border-radius: 10px;
    background: linear-gradient(170deg, var(--screen-a) 0%, var(--screen-b) 45%, var(--body-b) 62%, var(--body-a) 100%);
  }

  /* wide banner */
  .banner--wide .headline { left: 60px; top: 94px; font-size: 31px; }
  .banner--wide .subline { left: 60px; top: 134px; font-size: 21px; }
  .banner--wide .cta { left: 110px; top: 197px; font-size: 20px; }
  .banner--wide .laptop-art { left: 560px; top: 50px; width: 236px; height: 240px; }

  /* box banner */
  .banner--box .headline { left: 30px; top: 122px; font-size: 26px; }
  .banner--box .subline { left: 0; width: 430px; top: 155px; font-size: 20px; text-align: center; }
  .banner--box .cta { left: 48px; top: 233px; font-size: 16px; }
  .banner--box .laptop-art { left: 420px; top: 80px; width: 200px; height: 255px; }
</style>
</head>
<body>
  <main class="canvas">
    <section class="banner banner--wide">
      <h1 class="headline">FOR SME BUSINESS ONLY !</h1>
      <p class="subline">Buy a new laptop with KWD Grant subsidy</p>
      <p class="cta"><span class="cta__brand">Pinloop</span><span>Message us to find out more</span></p>
      <div class="laptop-art" role="img" aria-label="Vector illustration of an open silver laptop with a bright blue gradient screen"></div>
    </section>

    <section class="banner banner--box">
      <h1 class="headline">FOR SME BUSINESS ONLY !</h1>
      <p class="subline">Buy a new laptop with<br>KWD Grant subsidy</p>
      <p class="cta"><span class="cta__brand">Pinloop</span><span>Message us to find out more</span></p>
      <div class="laptop-art" role="img" aria-label="Vector illustration of an open silver laptop with a bright blue gradient screen"></div>
    </section>
  </main>
</body>
</html>
```